Larkfield Rowhomes - Billboard design for our newly renovated townhome community

We have a 5' wide x 4' tall billboard at the entrance to our apartment community, that needs to have the acrylic insert replaced. It is a 2 sided sign, and we are planning to use the same image on both sides. We are called Larkfield Rowhomes, and have 48 townhomes that are all 2 bedroom, 1 1/2 bath. A few things we would like to get across on the signage: "Newly Renovated" "2 bed 1 1/2 bath" "Full size W/D in every home" " New Appliances" I've included our parent company's logo - this is the only image I could think of, but it might not be worth having it on the sign. We are in Colorado, so mountain theme could be nice and also sunshine/sun since we are called "Larkfield"

Industry/Entity Type

Apartment

Font styles to use
Sans Serif

Requirements
Must have
• Newly Renovated
2 bed 1 1/2 bath
Full size W/D in every home
Virtual Tours available
www.brambletonhomesco.example
855 - 413 - 9286
Nice to have
• We are located in Colorado - possibly mountain theme? Since our community is called "Larkfield Rowhomes" - anything bright with Sun / Sunshine might look really nice as well.

```html
<!DOCTYPE html>
<html lang="en">
<head>
<meta charset="utf-8">
<title>Larkfield Rowhomes – Entrance Billboard</title>
<link rel="stylesheet" href="https://fonts.googleapis.com/css2?family=Open+Sans:wght@400;600;700;800&display=swap">
<style>
  :root {
    --red: #ee1b24;
    --ink: #3a3a3a;
    --black: #050505;
    --white: #ffffff;
    --stage: #ececec;
    --panel-grey: #e9e9e9;
  }
  * { margin: 0; padding: 0; box-sizing: border-box; }
  html, body {
    width: 1200px; height: 1200px; overflow: hidden;
    background: var(--stage);
    font-family: "Open Sans", Arial, sans-serif;
  }
  .billboard {
    position: absolute; left: 0; top: 120px;
    width: 1200px; height: 960px;
    background: var(--white);
    overflow: hidden;
  }
  .billboard__art { position: absolute; inset: 0; }
  .brand {
    position: absolute; left: 40px; top: 170px; width: 470px;
    display: flex; align-items: center; justify-content: center; gap: 12px;
    white-space: nowrap;
  }
  .brand__mark {
    flex: none;
    width: 26px; height: 26px; border-radius: 50%;
    background: var(--ink);
  }
  .brand__name {
    font-size: 30px; font-weight: 600; color: var(--ink); letter-spacing: 0.3px;
  }
  .headline {
    position: absolute; left: 30px; top: 280px; width: 500px;
    text-align: center; color: var(--ink);
    font-weight: 800; font-size: 73px; line-height: 78px; letter-spacing: 0.5px;
    text-transform: uppercase;
  }
  .badge {
    position: absolute; left: 58px; top: 464px; width: 442px; height: 74px;
    background: var(--red); border-radius: 37px;
    color: var(--white); font-weight: 700; font-size: 43px;
    display: flex; align-items: center; justify-content: center;
  }
  .features { position: absolute; left: 56px; top: 568px; list-style: none; }
  .features__item {
    display: flex; align-items: center; height: 59px;
    font-size: 38px; font-weight: 600; color: var(--ink);
    white-space: nowrap;
  }
  .features__icon { width: 30px; height: 30px; margin-right: 34px; flex: none; }
  .contact-phone {
    position: absolute; left: 70px; top: 840px; height: 120px;
    display: flex; align-items: center; gap: 18px;
    color: var(--white); font-weight: 700; font-size: 62px; letter-spacing: -0.5px;
    white-space: nowrap;
  }
  .contact-web {
    position: absolute; left: 598px; right: 24px; top: 840px; height: 120px;
    display: flex; align-items: center; gap: 14px;
    color: var(--white); font-weight: 700; font-size: 29px;
    white-space: nowrap;
  }
  .contact-web svg { flex: none; }
</style>
</head>
<body>
  <main class="billboard">
    <svg class="billboard__art" width="1200" height="960" viewBox="0 0 1200 960">
      <defs>
        <linearGradient id="panelShade" x1="0" y1="0" x2="1" y2="1">
          <stop offset="0" stop-color="#ffffff"/>
          <stop offset="0.5" stop-color="#e9e9e9"/>
          <stop offset="1" stop-color="#ffffff"/>
        </linearGradient>
        <linearGradient id="sceneTones" x1="0" y1="0" x2="0" y2="1">
          <stop offset="0" stop-color="#1556c2"/>
          <stop offset="0.3" stop-color="#4f86d6"/>
          <stop offset="0.42" stop-color="#6b6f7e"/>
          <stop offset="0.6" stop-color="#7d8a3a"/>
          <stop offset="0.72" stop-color="#c9b21e"/>
          <stop offset="0.85" stop-color="#2c4a22"/>
          <stop offset="1" stop-color="#16301a"/>
        </linearGradient>
      </defs>
      <rect x="0" y="0" width="640" height="840" fill="url(#panelShade)" opacity="0.7"/>
      <circle cx="960" cy="352" r="428" fill="none" stroke="#ee1b24" stroke-width="2"/>
      <circle cx="960" cy="352" r="392" fill="url(#sceneTones)" role="img"
              aria-label="Photo of Colorado mountain peaks above a valley of golden aspens and evergreen forest under a blue sky"/>
      <rect x="0" y="840" width="640" height="120" fill="#ee1b24"/>
      <path d="M 640 840 H 1200 V 960 H 640 A 62 62 0 0 1 578 898 A 58 58 0 0 1 640 840 Z" fill="#050505"/>
    </svg>

    <div class="brand">
      <span class="brand__mark"></span>
      <span class="brand__name">Crestline Communities</span>
    </div>

    <h1 class="headline">Larkfield<br>Rowhomes</h1>

    <div class="badge">Newly Renovated</div>

    <ul class="features">
      <li class="features__item">
        <svg class="features__icon" viewBox="0 0 30 30"><circle cx="15" cy="15" r="12" fill="none" stroke="#555" stroke-width="2"/><path d="M9 15 l5 5 l11 -12" fill="none" stroke="#ee1b24" stroke-width="2.5" stroke-linecap="round"/></svg>
        New Appliances
      </li>
      <li class="features__item">
        <svg class="features__icon" viewBox="0 0 30 30"><circle cx="15" cy="15" r="12" fill="none" stroke="#555" stroke-width="2"/><path d="M9 15 l5 5 l11 -12" fill="none" stroke="#ee1b24" stroke-width="2.5" stroke-linecap="round"/></svg>
        2 bed 1 1/2 bath
      </li>
      <li class="features__item">
        <svg class="features__icon" viewBox="0 0 30 30"><circle cx="15" cy="15" r="12" fill="none" stroke="#555" stroke-width="2"/><path d="M9 15 l5 5 l11 -12" fill="none" stroke="#ee1b24" stroke-width="2.5" stroke-linecap="round"/></svg>
        Full size W/D in every home
      </li>
      <li class="features__item">
        <svg class="features__icon" viewBox="0 0 30 30"><circle cx="15" cy="15" r="12" fill="none" stroke="#555" stroke-width="2"/><path d="M9 15 l5 5 l11 -12" fill="none" stroke="#ee1b24" stroke-width="2.5" stroke-linecap="round"/></svg>
        Virtual Tours available
      </li>
    </ul>

    <div class="contact-phone">
      <svg width="52" height="52" viewBox="0 0 24 24" aria-hidden="true">
        <path fill="#ffffff" d="M6.6 10.8c1.4 2.8 3.8 5.1 6.6 6.6l2.2-2.2c.3-.3.7-.4 1-.2 1.1.4 2.3.6 3.6.6.6 0 1 .4 1 1V20c0 .6-.4 1-1 1C10.6 21 3 13.4 3 4c0-.6.4-1 1-1h3.5c.6 0 1 .4 1 1 0 1.3.2 2.5.6 3.6.1.3 0 .7-.2 1z"/>
        <path fill="none" stroke="#ffffff" stroke-width="1.6" stroke-linecap="round" d="M14 3.5a6.5 6.5 0 0 1 6.5 6.5M14 7a3 3 0 0 1 3 3"/>
      </svg>
      <span>855-413-9286</span>
    </div>

    <div class="contact-web">
      <svg width="36" height="36" viewBox="0 0 42 42" aria-hidden="true">
        <circle cx="21" cy="21" r="19" fill="none" stroke="#ffffff" stroke-width="2"/>
        <circle cx="21" cy="21" r="11" fill="none" stroke="#ffffff" stroke-width="1.6"/>
        <ellipse cx="21" cy="21" rx="5" ry="11" fill="none" stroke="#ffffff" stroke-width="1.4"/>
        <path d="M10 21 H32 M12 15.5 H30 M12 26.5 H30" stroke="#ffffff" stroke-width="1.4"/>
      </svg>
      <span>www.brambletonhomesco.example</span>
    </div>
  </main>
</body>
</html>
```